Gobo Flyer to generate sales and to use at trade shows or as a leave behind to client

We are looking to create a flyer to promote our new exterior or interior event lighting options. We are looking for the layout to be clean and consistent with our color scheme. We are a professional technologically advanced company looking to take your event to the next level. We are looking for a layout which has an image at the top as well as a few other images to allow reader to see a few options

Target Market(s)

Residential as well as commercial

Industry/Entity Type

Trade

Requirements
Must have
• Need the round images to create a collage. and include the text samples of what is available

```html
<!DOCTYPE html>
<html lang="en">
<head>
<meta charset="utf-8">
<title>Lumen Nights Flyer</title>
<link href="https://fonts.googleapis.com/css2?family=Russo+One&family=Arimo:wght@400;700&display=swap" rel="stylesheet">
<style>
  :root {
    --backdrop: #e3dfdf;
    --paper: #ffffff;
    --brand-red: #d60027;
    --ink: #111111;
    --butter: #faf6a2;
    --peach: #f2a07a;
    --price-yellow: #ffe600;
    --white: #ffffff;
  }
  * { margin: 0; padding: 0; box-sizing: border-box; }
  html, body {
    width: 1098px; height: 1200px; overflow: hidden;
    background: var(--backdrop);
    font-family: "Arimo", Arial, sans-serif;
  }
  .flyer {
    position: absolute; left: 161px; top: 50px;
    width: 776px; height: 1100px;
    background: var(--paper);
    overflow: hidden;
  }
  .flyer__art { position: absolute; inset: 0; width: 776px; height: 1100px; }
  .brand-name {
    position: absolute; left: 0; top: 72px; width: 776px;
    text-align: center;
    font-family: "Arimo", Arial, sans-serif; font-weight: 700;
    font-size: 72px; line-height: 80px;
    color: var(--brand-red);
  }
  .tagline {
    position: absolute; left: 0; top: 166px; width: 776px;
    text-align: center;
    font-size: 24px; color: var(--ink);
  }
  .intro {
    position: absolute; left: 92px; top: 762px; width: 445px;
    font-size: 15px; line-height: 20px; font-weight: 700; color: var(--white);
  }
  .events-heading {
    position: absolute; left: 92px; top: 857px; width: 450px; height: 38px;
    border-top: 3px solid var(--ink); border-bottom: 3px solid var(--ink);
    font-size: 24px; line-height: 32px; font-weight: 400; color: var(--ink);
  }
  .events-list { list-style: none; position: absolute; top: 904px; font-size: 20px; font-weight: 700; color: var(--white); }
  .events-list li { height: 28.5px; position: relative; padding-left: 22px; white-space: nowrap; }
  .events-list li::before {
    content: "\2605"; position: absolute; left: 0; top: 2px;
    font-size: 14px; color: var(--ink);
  }
  .events-list--left { left: 69px; }
  .events-list--right { left: 364px; }
  .contact {
    position: absolute; left: 92px; top: 1026px;
    font-size: 14px; line-height: 20px; font-weight: 700; font-style: normal; color: var(--white);
  }
  .phone {
    position: absolute; left: 504px; top: 1040px;
    display: flex; align-items: center; gap: 10px;
    font-size: 33px; font-weight: 700; color: var(--white);
  }
  .phone__dot {
    width: 32px; height: 32px; border-radius: 50%;
    border: 3px solid var(--white);
  }
</style>
</head>
<body>
<main class="flyer">
  <svg class="flyer__art" viewBox="0 0 448 635" preserveAspectRatio="none">
    <defs>
      <linearGradient id="night-house-top" x1="0" y1="0" x2="1" y2="1">
        <stop offset="0" stop-color="#1a0a1e"/>
        <stop offset="0.45" stop-color="#7a2a86"/>
        <stop offset="1" stop-color="#120810"/>
      </linearGradient>
      <linearGradient id="night-house-bottom" x1="0" y1="0" x2="1" y2="0.6">
        <stop offset="0" stop-color="#3a1a24"/>
        <stop offset="0.35" stop-color="#a04a9a"/>
        <stop offset="0.7" stop-color="#5a48b0"/>
        <stop offset="1" stop-color="#0e1216"/>
      </linearGradient>
    </defs>
    <path class="blob-butter" d="M62 228 C92 192 152 205 162 262 L152 410 L44 410 C30 340 36 268 62 228Z" fill="var(--butter)"/>
    <rect class="band-red" x="0" y="407" width="448" height="180" fill="var(--brand-red)"/>
    <rect class="band-footer" x="0" y="587" width="448" height="48" fill="var(--ink)"/>
    <path class="blob-peach" d="M345 430 C370 410 420 418 423 455 C426 495 395 510 360 505 C330 500 328 450 345 430Z" fill="var(--peach)"/>
    <path role="img" aria-label="Photo of a house front lit in purple and pink projected lights at night"
          d="M172 170 C200 126 300 116 362 134 C402 150 400 230 382 268 L158 288 C144 242 152 202 172 170Z"
          fill="url(#night-house-top)"/>
    <path role="img" aria-label="Photo of a house with patterned gobo lighting, purple wall washers and a blue lit tree"
          d="M68 302 C110 272 250 266 332 290 C402 320 412 420 392 458 C360 470 330 472 310 462 C290 440 250 432 200 428 C140 420 90 390 72 350 C64 330 62 314 68 302Z"
          fill="url(#night-house-bottom)" opacity="0.96"/>
    <g class="price-tag">
      <path d="M286 252 H391 V357 H377 L378 388 L355 357 H286 Z" fill="var(--brand-red)" stroke="var(--white)" stroke-width="3" stroke-linejoin="round"/>
      <text x="297" y="287" font-family="Russo One, sans-serif" font-size="24" fill="var(--price-yellow)">$399</text>
      <text font-family="Russo One, sans-serif" font-size="11" fill="var(--ink)">
        <tspan x="297" y="306">FOR A</tspan>
        <tspan x="297" y="322">ONE NIGHT</tspan>
        <tspan x="297" y="338">RENTAL</tspan>
      </text>
    </g>
  </svg>

  <h1 class="brand-name">Lumen Nights</h1>
  <div class="tagline">Anytime you want to celebrate</div>

  <p class="intro">Illuminate a projected light design and 2 colored wall washers on the exterior or interior of your home business or special event.&nbsp; Choose from many stock designs or customize the image to make the design truly your own.</p>

  <h2 class="events-heading">Perfect for Special Events</h2>
  <ul class="events-list events-list--left">
    <li>Perfect for Special Events</li>
    <li>Parties</li>
    <li>Graduation</li>
  </ul>
  <ul class="events-list events-list--right">
    <li>Holidays</li>
    <li>Weddings</li>
    <li>Business Promotions</li>
  </ul>

  <address class="contact">
    Address will place here<br>
    details goes here | Email will place here<br>
    web details please
  </address>
  <div class="phone"><span class="phone__dot"></span>9999 99 999</div>
</main>
</body>
</html>
```